Ferncastle Holdings - stationery for luxury, exclusive property investment company

We need stationery (letterhead, folder, compliments slip and envelope) and business cards which will reflect our luxury brand.

I have attached some design examples that we like.

We are an investment company which buys property to provide accommodation for corporate customers.

The design of the stationery needs to be be simple, refined, understated, luxury and very tasteful.

The design should communicate luxury and exclusivity, without being ostentatious.

Logo files are attached

Please can designers re-read the brief, and make sure the logo is in gold on either on a navy or white background.

Target Market(s)

Wealthy customers

Contact Information for Business Card

Helen Travers-Booth
Director
Ferncastle Holdings Limited
email: helen@ferncastleholdings.co.uk
mob: 07712645930

Font styles to use
Serif

Colors

Designer to choose colors to be used in the design.

Requirements
Must have
• The logo must be gold on either a white or navy background as per the attached logos.
• The stationery MUST have the following information:
• Ferncastle Holdings Limited
• The Willows
• Ashby Rise
• Ashby
• GL52 7TN
• Company Number: 20418736 (Registered in England and Wales)
• The letterhead must also have the two attached logos for the PLG and the PLG accreditation scheme. They do not need to be large.
Nice to have
• A watermark, navy banding either top or bottom.
Should not have
• Anything that looks budget.

```html
<!DOCTYPE html>
<html lang="en">
<head>
<meta charset="utf-8">
<title>Ferncastle Holdings – Stationery</title>
<link href="https://fonts.googleapis.com/css2?family=Cinzel:wght@400&family=Questrial&family=Great+Vibes&display=swap" rel="stylesheet">
<style>
  :root{
    --bg:#ececec;
    --paper:#f8f8f7;
    --navy:#1d2940;
    --navy-light:#2c3b59;
    --gold:#b48c44;
    --gold-light:#e4c67e;
    --gold-deep:#a47c38;
    --grey-band:#8d8d8d;
    --ink:#4a4a4a;
    --ink-soft:#6b6b6b;
    --rule:#d6d6d6;
    --badge-red:#d9262e;
  }
  *{box-sizing:border-box;margin:0;padding:0}
  html,body{width:1200px;height:520px;overflow:hidden;background:var(--bg)}
  body{position:relative;font-family:"Questrial",sans-serif;color:var(--ink)}
  .piece{position:absolute;background:var(--paper);box-shadow:0 2px 6px rgba(0,0,0,.18)}

  .brand{font-family:"Cinzel",serif;font-weight:400;color:var(--gold);text-align:center;line-height:1}
  .brand .name{display:block;letter-spacing:.02em}
  .brand .sub{display:block;letter-spacing:.32em;margin-top:.3em}

  .gold-band{position:absolute;left:0;right:0;bottom:0;height:5px;
    background:linear-gradient(90deg,var(--gold-deep),var(--gold-light) 45%,var(--gold) 78%,var(--grey-band) 78.4%,var(--grey-band))}

  /* folder */
  .folder{left:47px;top:36px;width:350px;height:444px;
    background:radial-gradient(ellipse at 50% 48%,var(--navy-light) 0%,var(--navy) 70%)}
  .folder .spine{position:absolute;left:8px;top:0;bottom:0;width:18px;
    background:repeating-linear-gradient(90deg,rgba(228,198,126,.35) 0 1px,transparent 1px 5px)}
  .folder .brand{position:absolute;left:0;right:0;top:228px}
  .folder .brand .name{font-size:25px}
  .folder .brand .sub{font-size:12px}
  .folder .contact{position:absolute;left:0;right:0;bottom:18px;text-align:center;font-size:5.5px;color:var(--gold-light);line-height:1.7}

  /* letterhead */
  .letterhead{left:436px;top:65px;width:296px;height:415px}
  .letterhead .brand{position:absolute;left:24px;top:42px}
  .letterhead .brand .name{font-size:11px}
  .letterhead .brand .sub{font-size:5.5px}
  .letterhead .head-rule{position:absolute;left:24px;right:24px;top:66px;height:1px;background:var(--gold)}
  .letterhead .address{position:absolute;right:24px;top:41px;text-align:right;font-size:4.6px;line-height:1.45;color:var(--ink)}
  .letterhead .address .tel{display:block;margin-top:3px}
  .letterhead .salute{position:absolute;left:26px;top:115px;font-size:8px;color:var(--ink)}
  .letterhead .body{position:absolute;left:26px;right:24px;top:139px;font-size:4.6px;line-height:1.6;color:var(--ink-soft)}
  .letterhead .body p{margin-bottom:6px}
  .letterhead .signoff{display:block;margin-top:10px}
  .letterhead .badges{position:absolute;left:26px;bottom:20px;display:flex;gap:4px}
  .letterhead .reg{position:absolute;right:24px;bottom:22px;font-size:4.2px;color:var(--ink-soft);text-align:right}
  .badge{display:block;width:26px;height:12px;background:var(--badge-red)}

  /* business cards */
  .card-front{left:796px;top:60px;width:122px;height:69px}
  .card-front .brand{position:absolute;right:14px;top:9px}
  .card-front .brand .name{font-size:6px}
  .card-front .brand .sub{font-size:3px}
  .card-front .who{position:absolute;left:8px;top:35px;font-size:4.2px;color:var(--gold);letter-spacing:.04em;line-height:1.3}
  .card-front .role{display:block;font-size:2.8px;color:var(--ink-soft)}
  .card-front .rule{position:absolute;left:8px;right:8px;top:48px;height:1px;background:var(--rule)}
  .card-front .lines{position:absolute;left:8px;top:51px;font-size:2.8px;line-height:1.5;color:var(--ink)}
  .card-front .addr{position:absolute;right:8px;top:53px;font-size:2.8px;line-height:1.5;text-align:right;color:var(--ink)}
  .card-front .gold-band{height:3px}
  .card-back{left:937px;top:60px;width:100px;height:71px;
    background:radial-gradient(ellipse at 50% 45%,var(--navy-light),var(--navy) 75%)}
  .card-back .brand{position:absolute;left:0;right:0;top:29px}
  .card-back .brand .name{font-size:6.5px}
  .card-back .brand .sub{font-size:3.2px}
  .card-back .badge{position:absolute;right:8px;top:7px;width:12px;height:5px}
  .card-back .web{position:absolute;left:0;right:0;bottom:6px;text-align:center;font-size:2.8px;letter-spacing:.2em;color:var(--gold-light)}

  /* envelope */
  .envelope{left:771px;top:148px;width:342px;height:156px}
  .envelope .brand{position:absolute;left:26px;top:40px}
  .envelope .brand .name{font-size:10px}
  .envelope .brand .sub{font-size:5px}
  .envelope .address{position:absolute;left:18px;top:61px;font-size:4.8px;line-height:1.4;color:var(--ink)}

  /* compliments slip */
  .compliments{left:767px;top:326px;width:342px;height:156px}
  .compliments .brand{position:absolute;left:21px;top:41px}
  .compliments .brand .name{font-size:10px}
  .compliments .brand .sub{font-size:5px}
  .compliments .address{position:absolute;left:170px;top:33px;width:89px;text-align:right;font-size:4.6px;line-height:1.45;color:var(--ink);padding-right:6px;border-right:1px solid var(--rule)}
  .compliments .contact{position:absolute;left:264px;top:33px;font-size:4.6px;line-height:1.45;color:var(--ink)}
  .compliments .contact svg{width:4px;height:4px;vertical-align:-0.5px;margin-right:3px;fill:var(--gold)}
  .compliments .greeting{position:absolute;left:0;right:28px;top:102px;text-align:right;font-family:"Great Vibes",cursive;font-size:24px;color:var(--gold)}
</style>
</head>
<body>

  <section class="piece folder" aria-label="Presentation folder">
    <div class="spine"></div>
    <div class="brand"><span class="name">FERNCASTLE</span><span class="sub">HOLDINGS</span></div>
    <div class="contact">
      P: 07712645930 E: helen@ferncastleholdings.co.uk W: www.ferncastleholdings.co.uk<br>
      Ferncastle Holdings Limited The Willows Ashby Rise, Ashby GL52 7TN<br>
      Company Number: 20418736 (Registered in England and Wales)
    </div>
  </section>

  <section class="piece letterhead" aria-label="Letterhead">
    <div class="brand"><span class="name">FERNCASTLE</span><span class="sub">HOLDINGS</span></div>
    <div class="address">
      Ferncastle Holdings Limited<br>The Willows Ashby Rise, Ashby GL52 7TN
      <span class="tel">P. 07712645930 E. helen@ferncastleholdings.co.uk W. www.ferncastleholdings.co.uk</span>
    </div>
    <div class="head-rule"></div>
    <p class="salute">Dear Mr. Hale,</p>
    <div class="body">
      <p>Thank you for your continued interest in our residential portfolio. We are pleased to confirm that the corporate apartments discussed at our recent meeting remain available for long term lease from the start of next quarter.</p>
      <p>Each property is furnished to a high standard and managed by our own team, so your staff can settle in quickly and enjoy a calm, well kept home during their stay.</p>
      <p>We would be glad to arrange a private viewing at a time that suits you. Please let us know your preferred dates and we will make the necessary arrangements.</p>
      <p>Should you have any questions in the meantime, do not hesitate to contact me directly by phone or email.</p>
      <span class="signoff">Sincerely,</span>
    </div>
    <div class="badges"><span class="badge"></span><span class="badge"></span></div>
    <p class="reg">Company Number: 20418736<br>Registered in England and Wales</p>
    <div class="gold-band"></div>
  </section>

  <section class="piece card-front" aria-label="Business card front">
    <div class="brand"><span class="name">FERNCASTLE</span><span class="sub">HOLDINGS</span></div>
    <div class="who">HELEN TRAVERS-BOOTH<span class="role">DIRECTOR</span></div>
    <div class="rule"></div>
    <div class="lines">07712645930<br>helen@ferncastleholdings.co.uk<br>www.ferncastleholdings.co.uk</div>
    <div class="addr">The Willows, Ashby<br>Rise, Ashby GL52 7TN</div>
    <div class="gold-band"></div>
  </section>

  <section class="piece card-back" aria-label="Business card back">
    <span class="badge"></span>
    <div class="brand"><span class="name">FERNCASTLE</span><span class="sub">HOLDINGS</span></div>
    <div class="web">WWW.FERNCASTLEHOLDINGS.CO.UK</div>
  </section>

  <section class="piece envelope" aria-label="Envelope">
    <div class="brand"><span class="name">FERNCASTLE</span><span class="sub">HOLDINGS</span></div>
    <div class="address">Ferncastle Holdings Limited<br>The Willows Ashby Rise, Ashby GL52 7TN</div>
    <div class="gold-band"></div>
  </section>

  <section class="piece compliments" aria-label="Compliments slip">
    <div class="brand"><span class="name">FERNCASTLE</span><span class="sub">HOLDINGS</span></div>
    <div class="address">Ferncastle Holdings Limited<br>The Willows Ashby<br>Rise, Ashby GL52 7TN<br>Company No. 20418736</div>
    <div class="contact">
      <svg viewBox="0 0 10 10"><path d="M2 0h2l1 3-1.5 1a6 6 0 0 0 2.5 2.5L7 5l3 1v2a2 2 0 0 1-2 2A8 8 0 0 1 0 2a2 2 0 0 1 2-2z"/></svg>07712645930<br>
      <svg viewBox="0 0 10 10"><rect x="0" y="2" width="10" height="6"/></svg>helen@ferncastleholdings.co.uk<br>
      <svg viewBox="0 0 10 10"><circle cx="5" cy="5" r="5"/></svg>www.ferncastleholdings.co.uk
    </div>
    <p class="greeting">With Compliments</p>
    <div class="gold-band"></div>
  </section>

</body>
</html>
```